Bodywork Quietude Business Card Design

I want to create a very elegant and sophisticated two sided business card for my massage practice (www.bodyworkquietude.net). I have attached the logo and a PDF with some ideas down for the back of the card but I am open to suggestions. I will want to tie in a post card and flyer to the card later.
Similar colors to website would be great.
Target Market(s)
High end clientele, people looking for a sophisticated spa experience.
Industry/Entity Type
Massage
Contact Information for Business Card
Bodywork Quietude
7318 Larkspur Ave S, Suite 305
Alderbrook, OR 97321
(206) 555-0147
www.bodyworkquietude.net
Look and feel

```html
<!DOCTYPE html>
<html lang="en">
<head>
<meta charset="utf-8">
<title>Bodywork Quietude — Business Card</title>
<link rel="stylesheet" href="https://fonts.googleapis.com/css2?family=Cinzel:wght@400&family=Montserrat:wght@400&display=swap">
<style>
  :root {
    --backdrop: #2a2a2c;
    --ink-teal: #1b3241;
    --foil-gold: #cfae82;
    --contact-tan: #a88a62;
    --paper: #ffffff;
  }
  * { margin: 0; padding: 0; box-sizing: border-box; }
  html, body {
    width: 1200px;
    height: 930px;
    overflow: hidden;
    background: var(--backdrop);
  }
  .canvas {
    position: relative;
    width: 1200px;
    height: 930px;
  }
  .card {
    position: absolute;
    width: 600px;
    height: 343px;
    box-shadow: 0 14px 30px rgba(0, 0, 0, 0.45);
    overflow: hidden;
  }
  .card--front {
    left: 110px;
    top: 90px;
    background: var(--ink-teal);
  }
  .card--back {
    left: 490px;
    top: 497px;
    background: var(--paper);
  }
  .brand-name {
    position: absolute;
    left: 0;
    right: 0;
    text-align: center;
    font-family: "Cinzel", serif;
    font-weight: 400;
    font-size: 34px;
    letter-spacing: 0.02em;
    white-space: nowrap;
  }
  .card--front .brand-name {
    top: 150px;
    color: var(--foil-gold);
  }
  .card--back .brand-name {
    top: 92px;
    color: var(--ink-teal);
    font-size: 30px;
  }
  .contact {
    position: absolute;
    left: 120px;
    right: 20px;
    bottom: 78px;
    font-family: "Montserrat", sans-serif;
    font-style: normal;
    font-size: 15px;
    line-height: 1.5;
    color: var(--contact-tan);
    white-space: nowrap;
  }
  .contact__line { display: block; }
  .band {
    position: absolute;
    left: 0;
    right: 0;
    bottom: 0;
    height: 62px;
    background: var(--ink-teal);
  }
</style>
</head>
<body>
  <main class="canvas">
    <section class="card card--front" aria-label="Card front">
      <p class="brand-name">Bodywork Quietude</p>
    </section>

    <section class="card card--back" aria-label="Card back">
      <p class="brand-name">Bodywork Quietude</p>
      <address class="contact">
        <span class="contact__line">(206) 555-0147 | www.bodyworkquietude.net</span>
        <span class="contact__line">7318 Larkspur Ave S, Suite 305 Alderbrook, OR 97321</span>
      </address>
      <div class="band"></div>
    </section>
  </main>
</body>
</html>
```